International Accounting, Law and Real Estate firm needs a English-Spanish web design

We are a firm dedicated to accounting-taxes, Legal and Real Estate in the northern part of Mexico on the border with Arizona USA, so our clients are half Mexicans and Half Americans. We are located on the coast (Puerto Peñasco, also called Rocky Point). Our name is NOVA ADVISORY, where REAL stands for:
R=real
E= estate
A= Accounting
L= Legal
our web page is www.novaadvisory-demo.com.mx, we need something more attractive, profesional, fresh, inviting, and we need to have it in English and a Spanish and I need to be able to keep uploading new properties for sale.
Our number one activity now is Accounting and Taxes, we are growing on the legal side and there is a huge opportunity in the market to help Foreigners get their property titles, and our third activity is Real Estate. We have an excellent reputation of honesty and professional people. We would like to advertise as a ONE PLACE for Legal and Taxes matters. Or also something like Your Taxes and Trust specialists... or Total solutions with Integrity ....

Target Market(s)

local business and US visitors some of them do business in Mexico, others buy properties and need legal help to be able to get their title (which is done by a trust)

Industry/Entity Type

Real Estate

Number of Pages Required

3 page

Font styles to use
Serif
Sans Serif

Requirements
Must have
• Be in English and Spanish (I can help with translation English to Spanish); be able to update the real estate area since it changes accordingly to new listings and sales.
Nice to have
• Easy to navigate and to enter to each area of web page, we would have 3 areas the 1.- accounting and taxes
• 2.- Legal
• 3.- Real Estate

```html
<!DOCTYPE html>
<html lang="en">
<head>
<meta charset="utf-8">
<title>Nova Advisory – Real Estate, Accounting, Legal</title>
<link rel="stylesheet" href="https://fonts.googleapis.com/css2?family=Open+Sans:wght@300;400;600;700&family=Marcellus&display=swap">
<style>
:root{
  --orange:#f07b1a;
  --yellow:#f6c21c;
  --navy:#1f2a3a;
  --blue:#1a5fa8;
  --teal:#3bb7c9;
  --magenta:#b0176b;
  --pink:#e0197a;
  --ink:#222;
  --text:#555;
  --grey-band:#e9e9e9;
  --dark:#0d0d0d;
  --white:#fff;
}
*{box-sizing:border-box;margin:0;padding:0}
html,body{width:1200px;height:4072px;overflow:hidden}
body{font-family:"Open Sans",Arial,sans-serif;color:var(--text);background:var(--white);position:relative}
.serif{font-family:"Marcellus",Georgia,serif}
section,header,footer{position:absolute;left:0;width:1200px;overflow:hidden}
.abs{position:absolute}
.lorem{font-size:13px;line-height:19px;color:var(--text)}

/* header / hero */
.hero{top:0;height:795px;background:linear-gradient(180deg,#8fa6b8 0%,#b7b3a6 40%,#9c8a72 70%,#6b5a48 100%)}
.hero-photo{position:absolute;inset:0}
.main-nav{top:0;left:130px;width:740px;height:55px;background:var(--white);display:flex;align-items:center;padding-left:6px}
.main-nav a{font-size:14px;font-weight:600;color:#333;text-decoration:none;margin:0 14px;letter-spacing:.3px}
.main-nav a.active{border:1px solid #bbb;padding:14px 12px;margin:0 4px 0 0;border-bottom:3px solid var(--orange)}
.phone-box{top:0;left:869px;width:195px;height:55px;background:var(--blue);color:var(--white);font-size:14px;line-height:19px;padding:8px 0 0 60px}
.phone-box svg{position:absolute;left:14px;top:10px}
.account-bar{top:60px;left:815px;width:244px;height:32px;background:rgba(20,25,35,.85);border-bottom:3px solid var(--orange);color:var(--white);font-size:13px;display:flex;align-items:center;padding-left:38px;gap:8px}
.flag{display:inline-block;width:16px;height:11px;margin-left:6px}
.brand-box{top:114px;left:130px;width:402px;height:250px;background:var(--navy);text-align:center;padding-top:150px}
.brand-box .mark{position:absolute;left:171px;top:40px;width:60px;height:60px;background:var(--orange)}
.brand-name{font-family:"Marcellus",Georgia,serif;font-size:36px;color:var(--orange);letter-spacing:1px}
.brand-tag{font-size:12px;color:var(--white);font-weight:600;letter-spacing:1px;margin-top:4px}
.hero-title{top:448px;left:130px;font-size:60px;font-weight:300;line-height:62px;color:var(--white)}
.hero-sub{top:589px;left:130px;font-size:38px;font-weight:300;color:var(--white)}
.hero-btn{top:654px;height:66px;background:rgba(30,30,30,.75);color:var(--white);font-size:30px;font-weight:300;display:flex;align-items:center;padding-left:22px;gap:14px}
.dots{top:778px;left:141px;display:flex;gap:20px}
.dots span{width:44px;height:44px;border-radius:50%;color:var(--white);font-size:16px;font-weight:600;display:flex;align-items:center;justify-content:center}

/* services */
.services{top:800px;height:422px}
.service{position:absolute;top:74px;width:260px;text-align:center}
.service svg{display:block;margin:0 auto}
.service-label{font-family:"Marcellus",Georgia,serif;font-size:24px;color:#222;line-height:30px;margin-top:28px}

/* detail blocks */
.detail-acc{top:1222px;height:273px;background:var(--grey-band)}
.detail-legal{top:1495px;height:265px;background:var(--white)}
.detail h3{font-size:20px;font-weight:700;color:#111;position:absolute}
.photo{position:absolute}

/* search */
.search{top:1760px;height:548px;background:linear-gradient(135deg,#3a4250 0%,#6b7280 40%,#8a8f96 60%,#3b4048 100%)}
.search-panel{top:62px;left:130px;width:367px;height:364px;background:rgba(40,45,55,.7)}
.search-head{height:57px;background:var(--orange);color:var(--white);font-size:22px;padding:14px 0 0 24px}
.field{position:absolute;height:36px;border:1px solid #ccc;background:rgba(60,65,75,.8);color:#eee;font-size:12px;padding:9px 0 0 10px}
.field::after{content:"";position:absolute;right:12px;top:12px;width:7px;height:7px;border-right:2px solid #eee;border-bottom:2px solid #eee;transform:rotate(45deg)}
.search-btn{top:439px;left:440px;width:57px;height:57px;background:var(--orange)}
.want-title{position:absolute;top:74px;left:530px;font-size:42px;font-weight:300;color:var(--white);line-height:54px}
.want-text{position:absolute;top:134px;left:530px;width:545px;color:#eee}
.tab{top:222px;height:40px;color:var(--white);font-size:22px;display:flex;align-items:center;justify-content:center;width:95px}
.type-panel{top:262px;left:530px;width:534px;height:150px;background:rgba(30,33,40,.75)}
.type{position:absolute;top:24px;width:120px;text-align:center;color:var(--white);font-size:11px}

/* listings */
.listings{top:2308px;height:488px}
.tab-featured{top:54px;left:136px;width:298px;height:54px;background:var(--orange);color:var(--white);font-size:26px;display:flex;align-items:center;justify-content:center}
.tab-popular{top:68px;left:475px;font-size:26px;color:#222}
.tab-line{top:106px;left:136px;width:932px;height:2px;background:#ddd}
.card{position:absolute;top:144px;width:280px;height:294px;border:1px solid #e3e3e3}
.card .img{height:200px;position:relative}
.price{position:absolute;right:10px;bottom:8px;color:var(--white);font-size:22px;font-weight:700}
.card-title{font-family:"Marcellus",Georgia,serif;font-size:20px;color:var(--blue);padding:14px 0 0 12px;letter-spacing:.5px}
.card-foot{position:absolute;left:0;right:0;bottom:0;height:40px;border-top:1px solid #e3e3e3;font-size:12px;color:#333;display:flex;align-items:center;padding-left:12px;gap:24px}
.card-foot .go{position:absolute;right:0;top:0;width:46px;height:40px;background:var(--orange)}
.side-arrow{position:absolute}

/* videos */
.videos{top:2796px;height:544px;background:linear-gradient(180deg,#6a7a86 0%,#8c8f90 45%,#5c5a52 100%)}
.videos h2{position:absolute;top:50px;width:1200px;text-align:center;font-size:40px;color:var(--white);letter-spacing:2px;font-weight:400}
.videos p{position:absolute;top:130px;left:190px;width:815px;text-align:center;color:var(--white)}
.social{position:absolute;top:426px;width:54px;height:54px;border-radius:50%;background:rgba(255,255,255,.85)}

/* blog */
.blog{top:3340px;height:352px}
.blog h2{position:absolute;top:34px;width:1200px;text-align:center;font-size:40px;color:#222;font-weight:400;letter-spacing:2px}
.post{position:absolute;top:108px;width:300px}
.date{position:absolute;left:0;top:0;width:65px;height:73px;background:var(--blue);color:var(--white);text-align:center;font-size:18px;line-height:22px;padding-top:14px}
.post-title{position:absolute;left:79px;top:4px;font-size:19px;line-height:24px;color:#222}
.posted{position:absolute;left:79px;top:56px;font-size:9px;color:#888}
.post .lorem{position:absolute;left:0;top:88px;width:290px;color:#999;font-size:12px;line-height:17px}
.read{position:absolute;left:0;top:176px;font-size:11px;font-weight:700;color:var(--blue)}

/* footer */
.stripe{top:3692px;left:0;width:1200px;height:49px}
.footer{top:3741px;height:291px;background:var(--dark);color:var(--white)}
.footer h4{position:absolute;top:36px;font-family:"Marcellus",Georgia,serif;font-weight:400;font-size:17px;letter-spacing:1px}
.quick{position:absolute;top:70px;left:133px;list-style:none;font-size:12px;line-height:25px}
.about{position:absolute;top:66px;left:315px;width:280px;font-size:12px;line-height:19px}
.news-text{position:absolute;top:70px;left:641px;font-size:12px}
.input{position:absolute;left:641px;width:228px;height:33px;background:#333;font-size:12px;padding:8px 0 0 10px}
.submit{position:absolute;top:201px;left:641px;width:228px;height:34px;background:var(--orange);color:var(--white);font-weight:700;font-size:15px;text-align:center;padding-top:6px;letter-spacing:1px}
.foot-brand{position:absolute;top:50px;left:923px;width:190px;text-align:center}
.copyright{top:4032px;left:0;width:1200px;height:40px;background:#1a1a1a;color:#ddd;font-size:12px;text-align:center;line-height:40px}
</style>
</head>
<body>

<header class="hero">
  <div class="hero-photo" role="img" aria-label="Photo of a busy beach with seaside buildings and blue sky"></div>
  <nav class="main-nav abs">
    <a class="active" href="#">HOME</a><a href="#">REAL ESTATE</a><a href="#">ACCOUNTING</a><a href="#">LEGAL</a><a href="#">ABOUT US</a><a href="#">BLOG</a><a href="#">CONTACT</a>
  </nav>
  <div class="phone-box abs">
    <svg width="34" height="34" viewBox="0 0 34 34"><circle cx="17" cy="17" r="15" fill="none" stroke="#fff" stroke-width="2"/><path d="M12 10l3 0 2 5-2 1.5c1 2 2.5 3.5 4.5 4.5L21 19l5 2v3c-7 1-15-7-14-14z" fill="#fff"/></svg>
    US (555) 010 2040<br>MX (555) 019 7731
  </div>
  <div class="account-bar abs">Log in &nbsp;|&nbsp; Register <span class="flag" style="background:linear-gradient(#b22 0 33%,#fff 33% 66%,#236 66%)"></span><span class="flag" style="background:linear-gradient(90deg,#1a7a3a 0 33%,#fff 33% 66%,#c22 66%)"></span></div>
  <div class="brand-box abs">
    <span class="mark"></span>
    <div class="brand-name">NOVA ADVISORY</div>
    <div class="brand-tag">REAL ESTATE, ACCOUNTING, LEGAL</div>
  </div>
  <h1 class="hero-title abs">LOOKING FOR A LUXURIOUS<br>&amp; BEAUTIFUL HOME</h1>
  <p class="hero-sub abs">NOW IT'S EASY TO FIND YOUR FUTURE HOME</p>
  <a class="hero-btn abs" style="left:130px;width:318px">SELL YOUR HOME <svg width="30" height="30" viewBox="0 0 30 30"><circle cx="15" cy="15" r="13" fill="none" stroke="#fff" stroke-width="2"/><path d="M12 9l6 6-6 6z" fill="#fff"/></svg></a>
  <a class="hero-btn abs" style="left:489px;width:326px">BUY YOUR HOME <svg width="30" height="30" viewBox="0 0 30 30"><circle cx="15" cy="15" r="13" fill="none" stroke="#fff" stroke-width="2"/><path d="M12 9l6 6-6 6z" fill="#fff"/></svg></a>
</header>
<div class="dots abs" style="z-index:2"><span style="background:var(--pink)">1</span><span style="background:var(--magenta)">2</span><span style="background:#8a1552">3</span></div>

<section class="services">
  <div class="service" style="left:120px">
    <svg width="250" height="240" viewBox="0 0 260 250"><defs><linearGradient id="g1" x1="0" y1="0" x2="1" y2="1"><stop offset="0" stop-color="#f6c21c"/><stop offset="1" stop-color="#f07b1a"/></linearGradient></defs>
      <path d="M130 8L248 126 130 244 12 126z" fill="none" stroke="url(#g1)" stroke-width="14"/>
      <rect x="100" y="92" width="52" height="66" rx="4" fill="none" stroke="#222" stroke-width="5"/><path d="M110 108h32M110 122h32M110 136h22" stroke="#222" stroke-width="4"/><path d="M150 150l14 14" stroke="#222" stroke-width="6"/></svg>
    <div class="service-label">ACCOUNTING<br>&amp; TAXES</div>
  </div>
  <div class="service" style="left:470px">
    <svg width="250" height="240" viewBox="0 0 260 250"><defs><linearGradient id="g2" x1="0" y1="0" x2="1" y2="1"><stop offset="0" stop-color="#1a5fa8"/><stop offset="1" stop-color="#3bb7c9"/></linearGradient></defs>
      <path d="M130 8L248 126 130 244 12 126z" fill="none" stroke="url(#g2)" stroke-width="14"/>
      <circle cx="130" cy="126" r="34" fill="none" stroke="#222" stroke-width="6"/><path d="M113 124l13 13 26-28" fill="none" stroke="#222" stroke-width="8"/></svg>
    <div class="service-label">LEGAL</div>
  </div>
  <div class="service" style="left:812px">
    <svg width="250" height="240" viewBox="0 0 260 250"><defs><linearGradient id="g3" x1="0" y1="0" x2="1" y2="1"><stop offset="0" stop-color="#e0197a"/><stop offset="1" stop-color="#8a1552"/></linearGradient></defs>
      <path d="M130 8L248 126 130 244 12 126z" fill="none" stroke="url(#g3)" stroke-width="14"/>
      <path d="M108 160V100h20v60M128 160V84h18v76M146 160v-44h16v44M100 160h70" fill="#222" stroke="#222" stroke-width="3"/></svg>
    <div class="service-label">REAL ESTATE</div>
  </div>
</section>

<section class="detail detail-acc">
  <h3 style="left:136px;top:38px">ACCOUNTING &amp; TAXES</h3>
  <p class="lorem abs" style="left:136px;top:72px;width:484px">Lorem ipsum dolor sit amet, consectetuer adipiscing elit, sed diam nonummy nibh euismod tincidunt ut laoreet dolore magna aliquam erat volutpat. Ut wisi enim ad minim veniam, quis nostrud exerci tation ullamcorper suscipit lobortis nisl ut aliquip ex ea commodo consequat. Duis autem vel eum iriure dolor in hendrerit in vulputate velit esse molestie consequat, vel illum dolore eu feugiat nulla facilisis at vero eros et accumsan et iusto odio dignissim qui blandit praesent luptatum zzril delenit augue duis dolore te feugait nulla facilisi.</p>
  <div class="photo" style="left:676px;top:30px;width:375px;height:214px;background:linear-gradient(135deg,#f4f4f4,#b8bcc4 60%,#2b2f38);border:3px solid #fff" role="img" aria-label="Photo of hands working at a desk with keyboard and documents"></div>
</section>

<section class="detail detail-legal">
  <div class="photo" style="left:160px;top:25px;width:372px;height:207px;background:radial-gradient(circle at 70% 40%,#f8d9a0,#d98a2a 50%,#6b3a12)" role="img" aria-label="Photo of a wooden judge's gavel on warm background"></div>
  <h3 style="left:562px;top:34px">LEGAL</h3>
  <p class="lorem abs" style="left:562px;top:66px;width:484px">Lorem ipsum dolor sit amet, consectetuer adipiscing elit, sed diam nonummy nibh euismod tincidunt ut laoreet dolore magna aliquam erat volutpat. Ut wisi enim ad minim veniam, quis nostrud exerci tation ullamcorper suscipit lobortis nisl ut aliquip ex ea commodo consequat. Duis autem vel eum iriure dolor in hendrerit in vulputate velit esse molestie consequat, vel illum dolore eu feugiat nulla facilisis at vero eros et accumsan et iusto odio dignissim qui blandit praesent luptatum zzril delenit augue duis dolore te feugait nulla facilisi.</p>
</section>

<section class="search" role="img" aria-label="Blurred photo of a modern white residence">
  <div class="search-panel abs">
    <div class="search-head">Search Property</div>
    <div class="field" style="left:10px;top:106px;width:340px">Search Keyword</div>
    <div class="field" style="left:10px;top:160px;width:340px">Property Type</div>
    <div class="field" style="left:10px;top:214px;width:160px">Location</div>
    <div class="field" style="left:190px;top:214px;width:160px">Select Status</div>
    <div class="field" style="left:10px;top:269px;width:160px">Beds</div>
    <div class="field" style="left:190px;top:269px;width:160px">Baths</div>
    <div class="field" style="left:10px;top:323px;width:160px">$ Min Price</div>
    <div class="field" style="left:190px;top:323px;width:160px">$ Max Price</div>
  </div>
  <div class="search-btn abs"><svg width="57" height="57" viewBox="0 0 57 57"><circle cx="26" cy="26" r="9" fill="none" stroke="#fff" stroke-width="3"/><path d="M33 33l8 8" stroke="#fff" stroke-width="4"/></svg></div>
  <h2 class="want-title">I Want To...</h2>
  <p class="lorem want-text">Lorem ipsum dolor sit amet, consectetuer adipiscing elit, sed diam nonummy nibh euismod. Lorem ipsum dolor sit amet, consectetuer adipiscing elit, sed diam nonummy nibh euismod. Lorem ipsum dolor sit amet.</p>
  <div class="tab abs" style="left:530px;background:var(--orange)">Buy</div>
  <div class="tab abs" style="left:625px;background:#f4a35a">Sell</div>
  <div class="type-panel abs">
    <div class="type" style="left:5px"><svg width="60" height="60" viewBox="0 0 60 60"><path d="M8 28L30 10l22 18M14 26v26h32V26M24 52V38h12v14" fill="none" stroke="#fff" stroke-width="4"/></svg><br>VILLAS</div>
    <div class="type" style="left:138px"><svg width="60" height="60" viewBox="0 0 60 60"><path d="M10 54V14h24v40M34 24h16v30M6 54h48M16 22h4M24 22h4M16 32h4M24 32h4M16 42h4M24 42h4M40 32h4M40 42h4" fill="none" stroke="#fff" stroke-width="4"/></svg><br>APPARTMENTS</div>
    <div class="type" style="left:273px"><svg width="60" height="60" viewBox="0 0 60 60"><path d="M14 54V8h32v46M8 54h44M22 16h4M34 16h4M22 26h4M34 26h4M22 36h4M34 36h4M26 54V46h8v8" fill="none" stroke="#fff" stroke-width="4"/></svg><br>OFFICES</div>
    <div class="type" style="left:404px"><svg width="60" height="60" viewBox="0 0 60 60"><circle cx="30" cy="30" r="20" fill="none" stroke="#fff" stroke-width="4"/><path d="M10 30h40M30 10c-8 10-8 30 0 40M30 10c8 10 8 30 0 40" fill="none" stroke="#fff" stroke-width="3"/><circle cx="46" cy="42" r="6" fill="#fff"/></svg><br>LAND PLOTS</div>
  </div>
</section>

<section class="listings">
  <div class="tab-featured abs serif">FEATURED LISTING</div>
  <div class="tab-popular abs serif">MOST POPULAR</div>
  <div class="tab-line abs"></div>
  <svg class="side-arrow" style="left:70px;top:252px" width="30" height="90" viewBox="0 0 30 90"><path d="M28 2L2 45l26 43" fill="none" stroke="#ccc" stroke-width="2"/></svg>
  <svg class="side-arrow" style="left:1100px;top:252px" width="30" height="90" viewBox="0 0 30 90"><path d="M2 2l26 43-26 43" fill="none" stroke="#ccc" stroke-width="2"/></svg>
  <article class="card" style="left:133px">
    <div class="img" style="background:linear-gradient(180deg,#5aa8e0,#3fb8c8 55%,#c9b48a)" role="img" aria-label="Photo of a resort pool by the sea"><span class="price">$ 1,495,000</span></div>
    <div class="card-title">LOREM IPSUM DOLOR</div>
    <div class="card-foot"><span>◉ View Details</span><span>▣ Photos</span><span class="go"></span></div>
  </article>
  <article class="card" style="left:462px">
    <div class="img" style="background:linear-gradient(135deg,#c79a6a,#7a5436 50%,#e8dccb)" role="img" aria-label="Photo of a bedroom with wooden floor and window"><span class="price">$ 1,495,000</span></div>
    <div class="card-title">LOREM IPSUM DOLOR</div>
    <div class="card-foot"><span>◉ View Details</span><span>▣ Photos</span><span class="go"></span></div>
  </article>
  <article class="card" style="left:787px">
    <div class="img" style="background:linear-gradient(135deg,#6b8fc0,#4c6fa0 50%,#d8cdbd)" role="img" aria-label="Photo of a bedroom with blue walls"><span class="price">$ 1,495,000</span></div>
    <div class="card-title">LOREM IPSUM DOLOR</div>
    <div class="card-foot"><span>◉ View Details</span><span>▣ Photos</span><span class="go"></span></div>
  </article>
</section>

<section class="videos" role="img" aria-label="Photo of a modern house at dusk with palm trees">
  <h2 class="serif">FEATURED VIDEOS</h2>
  <p class="lorem">Lorem ipsum dolor sit amet, consectetuer adipiscing elit, sed diam nonummy nibh euismod tincidunt ut laoreet dolore magna aliquam erat volutpat. Ut wisi enim ad minim veniam, quis nostrud exerci tation ullamcorper suscipit lobortis nisl ut aliquip ex ea commodo consequat. Duis autem vel eum iriure dolor in hendrerit in vulputate velit esse molestie consequat.</p>
  <svg class="abs" style="left:532px;top:242px" width="130" height="130" viewBox="0 0 130 130"><circle cx="65" cy="65" r="60" fill="rgba(0,0,0,.15)" stroke="#fff" stroke-width="7"/><path d="M52 40l34 25-34 25z" fill="#fff"/></svg>
  <span class="social" style="left:323px"></span><span class="social" style="left:424px"></span><span class="social" style="left:524px"></span><span class="social" style="left:625px"></span><span class="social" style="left:725px"></span><span class="social" style="left:823px"></span>
</section>

<section class="blog">
  <h2 class="serif">LATEST BLOG POSTS</h2>
  <svg class="side-arrow" style="left:86px;top:110px" width="30" height="100" viewBox="0 0 30 100"><path d="M28 2L2 50l26 48" fill="none" stroke="#ccc" stroke-width="2"/></svg>
  <svg class="side-arrow" style="left:1098px;top:110px" width="30" height="100" viewBox="0 0 30 100"><path d="M2 2l26 48-26 48" fill="none" stroke="#ccc" stroke-width="2"/></svg>
  <article class="post" style="left:133px">
    <div class="date">20<br>JUNE</div>
    <div class="post-title">Lorem ipsum dolor sit amet, consectetuer</div>
    <div class="posted">posted by site admin</div>
    <p class="lorem">Lorem ipsum dolor sit amet, consectetuer adipiscing elit, sed diam nonummy nibh euismod tincidunt ut laoreet dolore magna aliquam erat volutpat.</p>
    <div class="read">READ MORE &gt;</div>
  </article>
  <article class="post" style="left:459px">
    <div class="date">19<br>JUNE</div>
    <div class="post-title">Lorem ipsum dolor sit amet, consectetuer</div>
    <div class="posted">posted by site admin</div>
    <p class="lorem">Lorem ipsum dolor sit amet, consectetuer adipiscing elit, sed diam nonummy nibh euismod tincidunt ut laoreet dolore magna aliquam erat volutpat.</p>
    <div class="read">READ MORE &gt;</div>
  </article>
  <article class="post" style="left:785px">
    <div class="date">18<br>JUNE</div>
    <div class="post-title">Lorem ipsum dolor sit amet, consectetuer</div>
    <div class="posted">posted by site admin</div>
    <p class="lorem">Lorem ipsum dolor sit amet, consectetuer adipiscing elit, sed diam nonummy nibh euismod tincidunt ut laoreet dolore magna aliquam erat volutpat.</p>
    <div class="read">READ MORE &gt;</div>
  </article>
</section>

<div class="stripe abs"><svg width="1200" height="49" viewBox="0 0 1200 49"><rect width="1200" height="49" fill="#f6c21c"/><path d="M0 0h640L600 49H0z" fill="#f07b1a"/></svg></div>

<footer class="footer">
  <h4 style="left:133px">QUICK LINKS</h4>
  <h4 style="left:315px">ABOUT US</h4>
  <h4 style="left:641px">NEWSLETTERS</h4>
  <ul class="quick"><li>HOME</li><li>REAL ESTATE</li><li>ACCOUNTING</li><li>LEGAL</li><li>ABOUT US</li><li>BLOG</li><li>CONTACT</li></ul>
  <p class="about">Lorem ipsum dolor sit amet, sed diam nonummy consectetuer adipiscing elit, sed diamdf nonummy nibh euismod tincidunt utfsd laoreet dolore magna aliquam erat volutpat. Ut wisi enim ad minim veniam, quis nostrud exerci tation ullamcorpers suscipit lobortis nisl ut aliquip.<br><span style="color:var(--orange);font-weight:700;font-size:11px">READ MORE &gt;</span></p>
  <p class="news-text">Lorem ipsum dolor sit amet, sed diam</p>
  <div class="input" style="top:106px">Name</div>
  <div class="input" style="top:155px">Phone</div>
  <div class="submit">SUBMIT</div>
  <div class="foot-brand"><span style="display:block;width:70px;height:70px;margin:0 auto 18px;background:var(--orange)"></span><span class="serif" style="font-size:20px;color:var(--orange)">NOVA ADVISORY</span></div>
</footer>
<div class="copyright abs">COPYRIGHT 2015 Novaadvisorymx | ALL RIGHTS RESERVED.</div>

</body>
</html>
```